Business Card Design

We need a cool business card for a new Beer Pong events and table sales company. We want it to be bright and fun. Maybe even have a table design on one side. Be creative and outgoing with it.

**I have attached a file that I have done as a potential idea, please think about it while designing**

Target Market(s)

18-40 year olds interested in playing drinking games

Industry/Entity Type

Events

Contact Information for Business Card

Carlton Cup Toss
info@carltoncuptoss.com.au
www.carltoncuptoss.com.au
www.facebook.com/carltoncuptoss
www.twitter.com/carltontoss

Font styles to use
Other font styles liked:
• College style font like in my file

```html
<!DOCTYPE html>
<html lang="en">
<head>
<meta charset="utf-8">
<title>Carlton Cup Toss — Business Card</title>
<link rel="stylesheet" href="https://fonts.googleapis.com/css2?family=Michroma&display=swap">
<style>
  :root {
    --backdrop: #e4e4e4;
    --card-white: #ffffff;
    --card-white-shade: #f1f1f1;
    --brand-green: #1d7f1a;
    --green-light: #2b8d22;
    --green-deep: #0a6c08;
    --ink: #1a1a1a;
    --text-on-green: #ffffff;
  }
  * { margin: 0; padding: 0; box-sizing: border-box; }
  html, body {
    width: 1200px;
    height: 750px;
    overflow: hidden;
    background: var(--backdrop);
  }
  .stage {
    position: relative;
    width: 1200px;
    height: 750px;
    display: flex;
    align-items: center;
    justify-content: center;
    gap: 60px;
  }
  .card {
    position: relative;
    width: 500px;
    height: 286px;
    border-radius: 30px;
    overflow: hidden;
    font-family: "Michroma", sans-serif;
    text-transform: uppercase;
  }
  /* Back: contact side */
  .card--contact {
    background: linear-gradient(135deg, var(--card-white) 55%, var(--card-white-shade));
  }
  .card--contact .top-band {
    position: absolute;
    top: 0; left: 0; right: 0;
    height: 16px;
    background: var(--brand-green);
  }
  .contact-block {
    position: absolute;
    left: 0; right: 0;
    top: 104px;
    text-align: center;
  }
  .contact-block .company-name {
    color: var(--brand-green);
    font-size: 19px;
    letter-spacing: 1px;
    margin-bottom: 8px;
  }
  .contact-block .contact-list {
    list-style: none;
    color: var(--ink);
    font-size: 9.5px;
    line-height: 14px;
    letter-spacing: 0.5px;
  }
  /* Front: brand side */
  .card--brand {
    background: linear-gradient(120deg, var(--green-light), var(--green-deep));
  }
  .card--brand .brand-name {
    position: absolute;
    left: 0; right: 0;
    top: 160px;
    text-align: center;
    color: var(--text-on-green);
    font-size: 17px;
    letter-spacing: 1px;
  }
  .card--brand .table-mark {
    position: absolute;
    right: 0;
    top: 0;
    width: 150px;
    height: 96px;
    background: linear-gradient(135deg, rgba(255,255,255,0.35), rgba(255,255,255,0.15));
  }
</style>
</head>
<body>
  <main class="stage">
    <section class="card card--contact">
      <div class="top-band"></div>
      <div class="contact-block">
        <h1 class="company-name">Carlton Cup Toss</h1>
        <ul class="contact-list">
          <li>info@carltoncuptoss.com.au</li>
          <li>www.carltoncuptoss.com.au</li>
          <li>www.facebook.com/carltoncuptoss</li>
          <li>www.twitter.com/carltontoss</li>
        </ul>
      </div>
    </section>

    <section class="card card--brand">
      <div class="table-mark" role="img" aria-label="White illustration of a beer pong table"></div>
      <h2 class="brand-name">Carlton Cup Toss</h2>
    </section>
  </main>
</body>
</html>
```